Web Design for Financial Consulting Company

We need a website design for a financial consulting company "Korvane Consulting". We build financial models, scenario analysis, handle the budgeting process and provide temporary staffing. I have over 10 years of experience. My Excel expertise and analytical savvy has saved clients over $17 million in profit.

Target Market(s)

Small to medium businesses

Industry/Entity Type

Financial Consulting

Number of Pages Required

4 page

Requirements
Must have
• Professional looking
Nice to have
• A little futuristic looking

```html
<!DOCTYPE html>
<html lang="en">
<head>
<meta charset="utf-8">
<title>Korvane Consulting</title>
<link href="https://fonts.googleapis.com/css2?family=Sora:wght@400;500;600;700&display=swap" rel="stylesheet">
<style>
:root{
  --ink:#14202b;
  --header:#1b2a35;
  --blue:#13a8e6;
  --violet:#4a4ee0;
  --mint:#4fd6a8;
  --yellow:#f5e12b;
  --soft:#f2f6f8;
  --card:#eaf0f4;
  --muted:#5b6670;
  --lilac:#c9c6f5;
  --stage:#0e0f12;
}
*{margin:0;padding:0;box-sizing:border-box}
html,body{width:762px;height:1200px;overflow:hidden;background:var(--stage);font-family:'Sora',sans-serif;color:var(--ink)}
.viewport{position:absolute;left:183px;top:29px;width:396px;height:1142px;overflow:hidden}
.page{position:absolute;left:0;top:0;width:793px;height:2284px;background:#fff;transform:scale(.5);transform-origin:0 0;overflow:hidden}
.abs{position:absolute}
.header{left:0;top:0;width:793px;height:55px;background:var(--header)}
.brand{display:flex;align-items:center;gap:6px;color:#fff;font-weight:600;font-size:17px;letter-spacing:1px;line-height:1}
.brand small{display:block;font-size:5px;letter-spacing:4px;color:var(--blue);font-weight:500;margin-top:2px}
.brand .mark{width:18px;height:18px;border:2px solid var(--blue)}
.nav{left:314px;top:22px;display:flex;gap:18px;font-size:10px;color:#fff}
.nav .active{color:var(--blue)}
.phone{left:578px;top:21px;color:#fff;font-size:10.5px;font-weight:600;display:flex;align-items:center;gap:5px}
.hero{left:0;top:55px;width:793px;height:310px;background:linear-gradient(100deg,var(--violet) 0%,#4f7fd0 45%,var(--mint) 100%)}
.hero-cut{left:0;top:300px}
.hero-title{left:126px;top:108px;color:#fff;font-size:26px;line-height:33px;font-weight:700}
.hero-title em{font-style:normal;color:var(--yellow)}
.checks{left:127px;top:228px;list-style:none;color:#fff;font-size:7.5px}
.checks li{display:flex;align-items:center;gap:8px;height:20px}
.tick{width:11px;height:11px;border-radius:50%;background:rgba(255,255,255,.35);display:inline-flex;align-items:center;justify-content:center}
.play{left:312px;top:227px;width:48px;height:48px;border-radius:50%;border:2px dashed rgba(255,255,255,.8);display:flex;align-items:center;justify-content:center}
.play span{width:38px;height:38px;border-radius:50%;background:#fff;display:flex;align-items:center;justify-content:center}
.quote{left:447px;top:100px;width:219px;height:227px;background:#fff;box-shadow:0 8px 24px rgba(0,0,0,.12)}
.quote .badge{left:21px;top:-22px;width:36px;height:36px;border-radius:50%;background:var(--yellow)}
.quote h3{left:21px;top:25px;font-size:15px;font-weight:700}
.quote .sub{left:21px;top:46px;font-size:6.5px;color:var(--muted)}
.field{left:21px;width:177px;height:22px;border-bottom:1px solid #d5dbe0;font-size:6.5px;color:var(--muted)}
.btn{background:var(--blue);color:#fff;font-weight:600;font-size:9.5px;border-radius:12px;display:flex;align-items:center;justify-content:center}
.social{left:695px;width:20px;height:20px}
.label{width:793px;text-align:center;font-size:7px;font-weight:700;color:var(--blue);letter-spacing:.3px;left:0}
.title{width:793px;text-align:center;font-size:22px;font-weight:700;line-height:26px;left:0}
.art{border-radius:10px}
.para{left:447px;top:545px;width:222px;font-size:7.5px;line-height:12px;color:var(--muted)}
.list{left:467px;top:616px;list-style:none;font-size:7.5px}
.list li{height:24px;display:flex;align-items:center;gap:9px}
.list .tick{background:#d9f2e6}
.works{left:0;top:782px;width:793px;height:518px;background:var(--soft);overflow:hidden}
.step{left:124px;width:260px}
.step .num{position:absolute;left:0;top:0;width:60px;height:60px;border-radius:50%;border:1.5px dashed #b9c4cc;background:#fff}
.step h4{position:absolute;left:78px;top:4px;font-size:10.5px;font-weight:700;line-height:13px;width:175px}
.step p{position:absolute;left:78px;top:34px;font-size:7px;line-height:12px;color:var(--muted);width:175px}
.logos{left:130px;top:1180px;width:534px;height:70px;display:flex;background:#fff}
.logos div{flex:1;border:1px solid #e2e8ec;display:flex;align-items:center;justify-content:center;font-size:10px;font-weight:600}
.member{width:170px;height:165px;background:var(--card)}
.avatar{position:absolute;left:20px;top:-42px;width:92px;height:92px;border-radius:50%;border:2px dashed #3bbf8a;padding:4px}
.avatar span{display:block;width:100%;height:100%;border-radius:50%;background:#6ff0c2}
.member .role{position:absolute;left:20px;top:62px;font-size:7px;font-weight:700;color:var(--blue)}
.member .name{position:absolute;left:20px;top:74px;font-size:11.5px}
.member .tel{position:absolute;left:20px;top:94px;font-size:7px;font-weight:600}
.member .follow{position:absolute;left:20px;top:114px;width:63px;height:22px;background:#fff;border:1px solid #dde3e7;font-size:7px;font-weight:600;display:flex;align-items:center;justify-content:center}
.testi{width:256px;height:175px;background:var(--soft)}
.testi p{position:absolute;left:56px;top:32px;width:186px;font-size:7.5px;line-height:12.5px;color:var(--muted)}
.testi .face{position:absolute;left:56px;top:118px;width:36px;height:36px;border-radius:50%;background:var(--blue)}
.testi b{position:absolute;left:102px;top:123px;font-size:10.5px}
.testi small{position:absolute;left:102px;top:139px;font-size:6.5px;color:var(--muted)}
.footer{left:0;top:1985px;width:793px;height:268px;background:var(--soft)}
.fcol h5{font-size:8px;font-weight:700;text-decoration:underline;margin-bottom:10px}
.fcol p{font-size:7px;line-height:12px;color:var(--muted)}
.bar{left:0;top:2253px;width:793px;height:31px;background:var(--header);color:#fff;font-size:7.5px;display:flex;align-items:center;justify-content:center}
</style>
</head>
<body>
<div class="viewport">
<div class="page">

  <header class="abs header">
    <div class="abs brand" style="left:128px;top:18px"><span class="mark"></span><span>KORVANE<small>CONSULTING</small></span></div>
    <nav class="abs nav"><span class="active">Home</span><span>About</span><span>Services ▾</span><span>Contact</span></nav>
    <div class="abs phone"><svg width="11" height="11" viewBox="0 0 12 12"><rect x="3" y="1" width="6" height="10" rx="1.5" fill="none" stroke="#13a8e6" stroke-width="1.2"/></svg>+1 555 0142 770</div>
  </header>

  <section class="abs hero"></section>
  <svg class="abs hero-cut" width="793" height="70" viewBox="0 0 793 70"><path d="M0 10 Q400 90 793 22 L793 70 L0 70 Z" fill="#fff"/></svg>
  <h1 class="abs hero-title">Helping your<br><em>Finance team</em> and<br>Increasing <em>Profit</em></h1>
  <ul class="abs checks">
    <li><span class="tick"><svg width="6" height="6" viewBox="0 0 6 6"><path d="M1 3l1.3 1.3L5 1.5" stroke="#fff" fill="none"/></svg></span>State of the art facility</li>
    <li><span class="tick"><svg width="6" height="6" viewBox="0 0 6 6"><path d="M1 3l1.3 1.3L5 1.5" stroke="#fff" fill="none"/></svg></span>Superior world class services</li>
    <li><span class="tick"><svg width="6" height="6" viewBox="0 0 6 6"><path d="M1 3l1.3 1.3L5 1.5" stroke="#fff" fill="none"/></svg></span>Certified and expert consultants.</li>
  </ul>
  <div class="abs play"><span><svg width="9" height="10" viewBox="0 0 9 10"><path d="M1 0L9 5L1 10Z" fill="#14202b"/></svg></span></div>

  <form class="abs quote">
    <span class="abs badge"></span>
    <h3 class="abs">Request a Quote</h3>
    <span class="abs sub">Marketing Business campaign</span>
    <div class="abs field" style="top:72px">Complete Name</div>
    <div class="abs field" style="top:105px">Email Address</div>
    <div class="abs field" style="top:139px">Phone No</div>
    <div class="abs btn" style="left:21px;top:180px;width:90px;height:24px">Start</div>
  </form>
  <span class="abs social" style="top:104px;background:#3b5998"></span>
  <span class="abs social" style="top:126px;background:#1da1f2"></span>
  <span class="abs social" style="top:148px;background:#e53935"></span>

  <p class="abs label" style="top:423px">WELCOME TO KORVANE CONSULTING</p>
  <h2 class="abs title" style="top:437px">Financial Analysis<br>Developing Meeting</h2>
  <div class="abs art" role="img" aria-label="Illustration of two consultants reviewing financial dashboards and charts" style="left:125px;top:510px;width:285px;height:240px;background:radial-gradient(circle at 55% 45%,var(--lilac),#eceafd 70%,#fff)"></div>
  <p class="abs para">Lorem ipsum dolor sit amet, consectetur adipiscing elit, sed do eiusmod tempor incididunt ut labore et dolore magna aliqua. Ut enim ad minim veniam, quis nostrud exercitation ullamco laboris nisi ut aliquip ex ea</p>
  <ul class="abs list">
    <li><span class="tick"><svg width="6" height="6" viewBox="0 0 6 6"><path d="M1 3l1.3 1.3L5 1.5" stroke="#3bbf8a" fill="none"/></svg></span>Get high conversion rates</li>
    <li><span class="tick"><svg width="6" height="6" viewBox="0 0 6 6"><path d="M1 3l1.3 1.3L5 1.5" stroke="#3bbf8a" fill="none"/></svg></span>Engage more users</li>
    <li><span class="tick"><svg width="6" height="6" viewBox="0 0 6 6"><path d="M1 3l1.3 1.3L5 1.5" stroke="#3bbf8a" fill="none"/></svg></span>Bring it to life again with us</li>
    <li><span class="tick"><svg width="6" height="6" viewBox="0 0 6 6"><path d="M1 3l1.3 1.3L5 1.5" stroke="#3bbf8a" fill="none"/></svg></span>Virtual Private Server (VPS)</li>
  </ul>

  <section class="abs works">
    <svg class="abs" style="left:0;top:0" width="793" height="518" viewBox="0 0 793 518">
      <circle cx="822" cy="92" r="70" fill="none" stroke="var(--blue)" stroke-width="18"/>
      <circle cx="-8" cy="280" r="42" fill="none" stroke="var(--blue)" stroke-width="14"/>
    </svg>
  </section>
  <p class="abs label" style="top:812px">HOW IT WORKS?</p>
  <h2 class="abs title" style="top:826px">Starting a Consulting Business<br>With No Experience</h2>
  <div class="abs step" style="top:900px"><span class="num"></span><h4>Analyze your market needs<br>and pain points.</h4><p>Enim ad minim veniam, quis rem ipsum nim veniam dolor sit amet ao.</p></div>
  <div class="abs step" style="top:980px"><span class="num"></span><h4>Develop your brand, and<br>service offerings.</h4><p>Enim ad minim veniam, quis rem ipsum nim veniam dolor sit amet ao.</p></div>
  <div class="abs step" style="top:1060px"><span class="num"></span><h4>Market your business to<br>attract new clients.</h4><p>Enim ad minim veniam, quis rem ipsum nim veniam dolor sit amet ao.</p></div>
  <div class="abs art" role="img" aria-label="Illustration of a founder working on a laptop beside a launching rocket and growth chart" style="left:400px;top:895px;width:260px;height:235px;background:radial-gradient(circle at 50% 45%,var(--lilac),#e7e6fb 65%,var(--soft))"></div>
  <div class="abs logos"><div>Tallow Row</div><div>Bramble Court</div><div>Quillo</div><div>Oakfen Works</div><div>Ferrow Roasters</div></div>
  <svg class="abs" style="left:560px;top:1258px" width="120" height="28" viewBox="0 0 120 28"><g stroke="var(--blue)" stroke-width="1.5"><line x1="0" y1="1" x2="115" y2="1"/><line x1="0" y1="9" x2="90" y2="9"/><line x1="0" y1="17" x2="110" y2="17"/><line x1="0" y1="25" x2="60" y2="25"/></g></svg>

  <p class="abs label" style="top:1352px">DEDICATED TO THE PEOPLE</p>
  <h2 class="abs title" style="top:1365px">Meet Our Expert Team</h2>
  <div class="abs member" style="left:127px;top:1448px"><span class="avatar" role="img" aria-label="Portrait avatar of consultant"><span></span></span><span class="role">EXPERT CONSULTANT</span><span class="name">Aldous Penrow</span><span class="tel">▯ +1 555 0193 418</span><span class="follow">Follow</span></div>
  <div class="abs member" style="left:310px;top:1448px"><span class="avatar" role="img" aria-label="Portrait avatar of consultant"><span></span></span><span class="role">EXPERT CONSULTANT</span><span class="name">Maren Colby</span><span class="tel">▯ +1 555 0193 418</span><span class="follow">Follow</span></div>
  <div class="abs member" style="left:493px;top:1448px"><span class="avatar" role="img" aria-label="Portrait avatar of consultant"><span></span></span><span class="role">EXPERT CONSULTANT</span><span class="name">Teodor Vance</span><span class="tel">▯ +1 555 0193 418</span><span class="follow">Follow</span></div>

  <p class="abs label" style="top:1656px">1M SATISFIED CUSTOMERS</p>
  <h2 class="abs title" style="top:1670px">What Client’s Say</h2>
  <div class="abs testi" style="left:137px;top:1718px"><p>“consultancy has been a very enjoyable and professional experience. The effort that Korvane Consulting puts in to ensure well trained consulting teams lead by well trained and knowledgeable team leaders is very evident.”</p><span class="face" role="img" aria-label="Client avatar"></span><b>Idris Calloway</b><small>Director of Information Technology</small></div>
  <div class="abs testi" style="left:405px;top:1718px"><p>“consultancy has been a very enjoyable and professional experience. The effort that Korvane Consulting puts in to ensure well trained consulting teams lead by well trained and knowledgeable team leaders is very evident.”</p><span class="face" role="img" aria-label="Client avatar"></span><b>Idris Calloway</b><small>Director of Information Technology</small></div>
  <svg class="abs" style="left:386px;top:1923px" width="22" height="8" viewBox="0 0 22 8"><circle cx="4" cy="4" r="3.5" fill="var(--blue)"/><circle cx="15" cy="4" r="3" fill="#c5cdd3"/></svg>

  <footer class="abs footer">
    <div class="abs brand" style="left:126px;top:55px;color:var(--ink)"><span class="mark"></span><span>KORVANE<small>CONSULTING</small></span></div>
    <div class="abs fcol" style="left:310px;top:50px;width:165px"><h5>INFORMATION</h5><p>Lorem ipsum dolor sit amet, consectetur adipiscing elit, sed do eiusmod tempor incididunt ut labore et dolore magna</p></div>
    <div class="abs fcol" style="left:493px;top:50px;width:180px"><h5>CONTACT US</h5><p>Phone: &nbsp;+1 555 0142 770<br>Email: &nbsp;hello@korvane.example</p></div>
    <h2 class="abs title" style="top:145px;font-size:26px">Start with Us</h2>
    <p class="abs" style="left:0;top:185px;width:793px;text-align:center;font-size:7px;color:var(--muted)">We help business innovate &amp; growth company with 10 Years Professional Experience</p>
    <div class="abs btn" style="left:351px;top:207px;width:90px;height:22px">Start</div>
  </footer>
  <div class="abs bar">2023 © Korvane Consulting Business. All Rights Reserved.</div>
  <svg class="abs" style="left:741px;top:2240px" width="30" height="30" viewBox="0 0 30 30"><circle cx="15" cy="15" r="14" fill="#fff" stroke="var(--blue)" stroke-width="2"/><path d="M15 21V10M11 14l4-4 4 4" stroke="var(--ink)" stroke-width="1.5" fill="none"/></svg>

</div>
</div>
</body>
</html>
```